Business Card Design

our business is purchasing, rehabbing and flipping homes. Design a house in the palm of a hand. This card is for a new company based in Georgia. So we buy homes that have been foreclosed, short sales,abandond, old homes and vacant homes.
We help improve the communities that we work in. We would like to see designs that use a black background with green accent and other colors that blend and don't take away from the logo and other important information.

Industry/Entity Type

Business

Contact Information for Business Card

Mavenbrook Holdings
Turning Old Doors Into New Starts
2738 Fenwick Lane
Duluth GA 30418
Office: 678-555-0192
mavenbrookholdingsllc.example

```html
<!DOCTYPE html>
<html lang="en">
<head>
<meta charset="utf-8">
<title>Mavenbrook Holdings – Business Card</title>
<link rel="stylesheet" href="https://fonts.googleapis.com/css2?family=Lora:wght@500;700&family=Tinos:ital@0;1&display=swap">
<style>
  :root {
    --card-black: #0b0b0b;
    --lime: #b5d334;
    --lime-deep: #8fb021;
    --white: #ffffff;
    --stage: #e8e5df;
    --photo-warm: #c9ad7a;
    --photo-dark: #3a3226;
  }
  * { margin: 0; padding: 0; box-sizing: border-box; }
  html, body { width: 1200px; height: 892px; overflow: hidden; background: var(--stage); }
  .stage { width: 1200px; height: 892px; display: flex; align-items: center; justify-content: center; }
  .card {
    position: relative; width: 1000px; height: 571px; overflow: hidden;
    background: radial-gradient(ellipse at 55% 30%, #1c1c1c 0%, var(--card-black) 65%);
    box-shadow: 0 10px 30px rgba(0,0,0,.25);
  }
  .swoosh { position: absolute; inset: 0; width: 1000px; height: 571px; }
  .brand { position: absolute; left: 60px; top: 40px; z-index: 1; }
  .brand-name {
    font-family: "Lora", serif; font-weight: 500; font-size: 58px;
    color: var(--lime); line-height: 1;
  }
  .brand-tagline {
    margin-top: 12px; font-family: "Tinos", serif; font-size: 19px;
    letter-spacing: 4.5px; color: var(--white);
  }
  .person { position: absolute; right: 70px; top: 142px; text-align: right; z-index: 1; }
  .person-name {
    font-family: "Lora", serif; font-weight: 700; font-size: 48px;
    color: var(--white); line-height: 1;
  }
  .person-title {
    margin-top: 8px; font-family: "Tinos", serif; font-style: italic;
    font-size: 21px; color: var(--lime);
  }
  .hero-photo {
    position: absolute; left: 30px; top: 300px; width: 250px; height: 271px;
    background: radial-gradient(ellipse at 45% 40%, var(--photo-warm) 0%, #a88c60 40%, var(--photo-dark) 80%, transparent 100%);
  }
  .contacts {
    position: absolute; left: 300px; top: 330px; list-style: none; z-index: 1;
    font-family: "Tinos", serif; font-size: 19px; color: var(--white);
  }
  .contact { display: flex; align-items: center; gap: 12px; height: 38px; white-space: nowrap; }
  .contact-icon {
    width: 24px; height: 24px; background: var(--lime); flex: none;
    display: flex; align-items: center; justify-content: center;
  }
  .contact-icon svg { width: 16px; height: 16px; }
</style>
</head>
<body>
<main class="stage">
  <section class="card">
    <svg class="swoosh" viewBox="0 0 1000 571" aria-hidden="true">
      <path fill="var(--white)" d="M1000,250 C870,258 800,320 745,410 C700,490 640,550 540,571 L1000,571 Z"/>
      <path fill="var(--card-black)" d="M1000,266 C880,274 815,334 762,422 C718,500 665,555 575,571 L1000,571 Z"/>
      <path fill="var(--lime)" d="M1000,276 C890,284 828,344 775,430 C732,506 682,558 600,571 L1000,571 Z"/>
      <path fill="var(--lime-deep)" opacity=".35" d="M1000,350 C900,368 845,430 805,500 C785,535 760,560 735,571 L1000,571 Z"/>
    </svg>

    <header class="brand">
      <h1 class="brand-name">Mavenbrook Holdings</h1>
      <p class="brand-tagline">Turning Old Doors Into New Starts</p>
    </header>

    <div class="person">
      <h2 class="person-name">Employee name</h2>
      <p class="person-title">Managing Director</p>
    </div>

    <div class="hero-photo" role="img" aria-label="Photo of a small model house resting in the palm of an open hand"></div>

    <ul class="contacts">
      <li class="contact">
        <span class="contact-icon">
          <svg viewBox="0 0 24 24"><path fill="#111" d="M6.6 10.8a15.1 15.1 0 0 0 6.6 6.6l2.2-2.2a1 1 0 0 1 1-.25 11.4 11.4 0 0 0 3.6.57 1 1 0 0 1 1 1V20a1 1 0 0 1-1 1A17 17 0 0 1 3 4a1 1 0 0 1 1-1h3.5a1 1 0 0 1 1 1c0 1.25.2 2.45.57 3.57a1 1 0 0 1-.25 1z"/></svg>
        </span>
        <span>678-555-0192</span>
      </li>
      <li class="contact">
        <span class="contact-icon">
          <svg viewBox="0 0 24 24" fill="none" stroke="#111" stroke-width="2"><circle cx="12" cy="12" r="9"/><path d="M3 12h18M12 3c3 3.2 3 14.8 0 18M12 3c-3 3.2-3 14.8 0 18"/></svg>
        </span>
        <span>www.mavenbrookholdingsllc.example</span>
      </li>
      <li class="contact">
        <span class="contact-icon">
          <svg viewBox="0 0 24 24"><path fill="#111" d="M12 2a7 7 0 0 0-7 7c0 5.2 7 13 7 13s7-7.8 7-13a7 7 0 0 0-7-7zm0 9.5A2.5 2.5 0 1 1 12 6.5a2.5 2.5 0 0 1 0 5z"/></svg>
        </span>
        <span>2738 Fenwick Lane Duluth GA 30418</span>
      </li>
    </ul>
  </section>
</main>
</body>
</html>
```